Commercial / Truck Battery Label

We need a high definition label design to send to a commercial printer for a Commercial/Truck Battery Label
I will upload our current truck battery label for you to get an idea of what we are looking for. Along with some competitor images and other logos for the label that we have on file. If we need to purchase a few images to make the label we can do that but need to see the design first.
The Labels need to have a plain white area which is 60mm Long x 40mm High along the bottom left corner. We will use this area for the battery specifications.
The Top Six Warning Icons downloaded also need to be on the label, perhaps along the bottom to the right of the white area in pairs. The icons size can be between 10mm x 10mm and 20mm x 20mm
The dimensions of the label need to be 390mm Long and the height needs to be both 140mm and 180mm. Same label 2 different sizes.
I would like to keep the terms : "SUPER HEAVY DUTY" and "THE STEADY CHARGE THAT ENDURES" on the label somewhere. Maybe replacing the word batteries or commercial with SUPER HEAVY DUTY under the right side of the VOLTRIXA Logo.
The labels will be used predominantly on Black batteries, so a colour scheme or design to suit that.
I don't mind a completely fresh design or a reworking of the old design.

```html
<!DOCTYPE html>
<html lang="en">
<head>
<meta charset="utf-8">
<title>VOLTRIXA Super Heavy Duty Battery Labels</title>
<link rel="stylesheet" href="https://fonts.googleapis.com/css2?family=Russo+One&display=swap">
<style>
  :root {
    --page-bg: #eeeeee;
    --panel-light: #fafafa;
    --panel-light-2: #cfcfd2;
    --brand-blue: #0c1f8a;
    --silver: #e9e9ec;
    --band-red: #e4121d;
    --ink: #111111;
    --icon-blue: #1746a2;
    --icon-red: #d81f26;
    --icon-yellow: #f5c400;
  }
  * { box-sizing: border-box; margin: 0; padding: 0; }
  html, body { width: 1200px; height: 1200px; overflow: hidden; background: var(--page-bg); }
  body { font-family: "Russo One", sans-serif; position: relative; }

  .sheet {
    position: absolute; left: 225px; top: 276px; width: 749px;
    display: flex; flex-direction: column; gap: 35px;
  }
  .label {
    position: relative; width: 749px; height: var(--h);
    border-radius: 4px; overflow: hidden;
    background: linear-gradient(180deg, var(--panel-light) 55%, var(--panel-light-2) 100%);
    box-shadow: 0 8px 14px rgba(0,0,0,.35);
  }
  .label--tall { --h: 345px; }
  .label--short { --h: 268px; }

  .label__backdrop { position: absolute; inset: 0; width: 100%; height: 100%; }

  .label__brand {
    position: absolute; white-space: nowrap; line-height: 1;
    font-size: calc(var(--h) * 0.17);
    letter-spacing: 3px;
    color: var(--silver);
  }
  .label__class {
    position: absolute; white-space: nowrap; line-height: 1;
    font-size: calc(var(--h) * 0.075);
    color: var(--silver); letter-spacing: 1px;
  }
  .label__tagline {
    position: absolute; display: flex; align-items: center; justify-content: flex-end;
    padding-right: 12px;
    background: linear-gradient(90deg, rgba(228,18,29,0) 0%, rgba(228,18,29,.55) 30%, var(--band-red) 65%);
  }
  .label__tagline span {
    font-size: calc(var(--h) * 0.052); color: var(--ink);
    letter-spacing: .5px; white-space: nowrap;
  }
  .label__vehicle {
    position: absolute;
    background: linear-gradient(160deg, rgba(190,190,200,.18), rgba(120,120,130,.05));
    border-radius: 6px;
  }
  .label__maker {
    position: absolute; display: flex; align-items: center; justify-content: flex-end; gap: 8px;
    font-size: calc(var(--h) * 0.085); color: var(--brand-blue); white-space: nowrap;
  }
  .label__maker i { display: block; width: calc(var(--h) * 0.06); height: calc(var(--h) * 0.06); background: var(--band-red); }
  .label__warnings {
    position: absolute; display: flex; align-items: center; justify-content: space-between;
  }
  .label__warnings svg { width: 28px; height: 28px; }
  .label__warnings .pb { font-family: Arial, sans-serif; font-weight: 700; font-size: 20px; color: var(--ink); }

  .label--tall .label__brand { left: 7%; top: 11%; }
  .label--tall .label__class { right: 31%; top: 28%; }
  .label--tall .label__tagline { left: 2%; width: 67%; top: 38.5%; height: 6%; }
  .label--tall .label__vehicle { left: 69.5%; top: 8%; width: 23%; height: 37%; }
  .label--tall .label__maker { right: 5%; top: 72%; }
  .label--tall .label__warnings { left: 27%; width: 40%; top: 84.5%; height: 9%; }

  .label--short .label__brand { left: 6%; top: 9%; }
  .label--short .label__class { right: 36%; top: 27.5%; }
  .label--short .label__tagline { left: 2%; width: 62%; top: 40%; height: 7%; }
  .label--short .label__vehicle { left: 66%; top: 7%; width: 19%; height: 41%; }
  .label--short .label__maker { right: 5%; top: 70%; }
  .label--short .label__warnings { left: 27%; width: 40%; top: 84%; height: 11%; }
</style>
</head>
<body>
<svg width="0" height="0" style="position:absolute" aria-hidden="true">
  <defs>
    <symbol id="ico-manual" viewBox="0 0 28 28"><circle cx="14" cy="14" r="13" fill="var(--icon-blue)"/><rect x="7" y="8" width="14" height="12" rx="1" fill="none" stroke="#fff" stroke-width="2"/><line x1="14" y1="8" x2="14" y2="20" stroke="#fff" stroke-width="1.5"/></symbol>
    <symbol id="ico-goggles" viewBox="0 0 28 28"><circle cx="14" cy="14" r="13" fill="var(--icon-blue)"/><circle cx="14" cy="11" r="5" fill="#fff"/><rect x="6" y="11" width="16" height="5" rx="2.5" fill="#fff" stroke="var(--icon-blue)" stroke-width="1"/></symbol>
    <symbol id="ico-prohibit" viewBox="0 0 28 28"><circle cx="14" cy="14" r="12" fill="#fff" stroke="var(--icon-red)" stroke-width="3"/><line x1="6" y1="6" x2="22" y2="22" stroke="var(--icon-red)" stroke-width="3"/></symbol>
    <symbol id="ico-caution" viewBox="0 0 28 28"><path d="M14 2 L27 25 H1 Z" fill="var(--icon-yellow)" stroke="#111" stroke-width="2" stroke-linejoin="round"/><rect x="12.8" y="10" width="2.4" height="8" fill="#111"/><rect x="12.8" y="20" width="2.4" height="2.4" fill="#111"/></symbol>
    <symbol id="ico-bin" viewBox="0 0 28 28"><rect x="8" y="7" width="12" height="15" fill="none" stroke="#111" stroke-width="1.5"/><line x1="6" y1="7" x2="22" y2="7" stroke="#111" stroke-width="1.5"/><line x1="4" y1="4" x2="24" y2="24" stroke="#111" stroke-width="1.5"/><line x1="24" y1="4" x2="4" y2="24" stroke="#111" stroke-width="1.5"/></symbol>
    <symbol id="ico-recycle" viewBox="0 0 28 28"><path d="M14 4 L23 20 H5 Z" fill="none" stroke="#111" stroke-width="1.6" stroke-linejoin="round"/><path d="M18 10 l2 -1 M8 16 l-1 2 M14 20 h2" stroke="#111" stroke-width="1.6"/></symbol>
  </defs>
</svg>

<main class="sheet">
  <section class="label label--tall" aria-label="VOLTRIXA label, 390 by 180 mm">
    <svg class="label__backdrop" viewBox="0 0 100 100" preserveAspectRatio="none" aria-hidden="true">
      <defs>
        <linearGradient id="dark-tall" x1="0" y1="0" x2="1" y2="1"><stop offset="0" stop-color="#2b2b2e"/><stop offset="1" stop-color="#161618"/></linearGradient>
      </defs>
      <path d="M0 0 H100 V38 C80 52 45 60 0 61 Z" fill="url(#dark-tall)"/>
      <path d="M0 62.5 C45 61.5 80 54 100 40.5" fill="none" stroke="#a9a9ae" stroke-width="3" vector-effect="non-scaling-stroke"/>
    </svg>
    <div class="label__brand">VOLTRIXA</div>
    <div class="label__class">SUPER HEAVY DUTY</div>
    <div class="label__tagline"><span>THE STEADY CHARGE THAT ENDURES</span></div>
    <div class="label__vehicle" role="img" aria-label="Line illustration of a box truck in side view"></div>
    <div class="label__maker"><i></i>KORVEN POWER</div>
    <div class="label__warnings" aria-label="Safety warning symbols">
      <svg><use href="#ico-manual"/></svg>
      <svg><use href="#ico-goggles"/></svg>
      <svg><use href="#ico-prohibit"/></svg>
      <svg><use href="#ico-caution"/></svg>
      <svg><use href="#ico-prohibit"/></svg>
      <svg><use href="#ico-caution"/></svg>
      <span class="pb">Pb</span>
      <svg><use href="#ico-bin"/></svg>
      <svg><use href="#ico-recycle"/></svg>
    </div>
  </section>

  <section class="label label--short" aria-label="VOLTRIXA label, 390 by 140 mm">
    <svg class="label__backdrop" viewBox="0 0 100 100" preserveAspectRatio="none" aria-hidden="true">
      <defs>
        <linearGradient id="dark-short" x1="0" y1="0" x2="1" y2="1"><stop offset="0" stop-color="#2b2b2e"/><stop offset="1" stop-color="#161618"/></linearGradient>
      </defs>
      <path d="M0 0 H100 V33 C80 50 45 60 0 61 Z" fill="url(#dark-short)"/>
      <path d="M0 63 C45 62 80 53 100 36" fill="none" stroke="#a9a9ae" stroke-width="3" vector-effect="non-scaling-stroke"/>
    </svg>
    <div class="label__brand">VOLTRIXA</div>
    <div class="label__class">SUPER HEAVY DUTY</div>
    <div class="label__tagline"><span>THE STEADY CHARGE THAT ENDURES</span></div>
    <div class="label__vehicle" role="img" aria-label="Line illustration of a box truck in side view"></div>
    <div class="label__maker"><i></i>KORVEN POWER</div>
    <div class="label__warnings" aria-label="Safety warning symbols">
      <svg><use href="#ico-manual"/></svg>
      <svg><use href="#ico-goggles"/></svg>
      <svg><use href="#ico-prohibit"/></svg>
      <svg><use href="#ico-caution"/></svg>
      <svg><use href="#ico-prohibit"/></svg>
      <svg><use href="#ico-caution"/></svg>
      <span class="pb">Pb</span>
      <svg><use href="#ico-bin"/></svg>
      <svg><use href="#ico-recycle"/></svg>
    </div>
  </section>
</main>
</body>
</html>
```